Kestrel Bridge Consulting (KBC) Business Card Design

I would like to create double-sided business cards that contain:
1) Name: Derek Molvane
2) Phone Number: +1 (555) 218-4907
3) Email: Derek.Molvane@KestrelBridgeConsulting.example
4) Website: KestrelBridgeConsulting.example

I would like to include my logo and a color scheme similar to the Varnholt Grand Prix Ostera squad color scheme (black, silver, greenish-blue – but can also include regular blue)

What we do: Our company develops and delivers innovative and pragmatic information technology and cybersecurity risk and compliance solutions for organizations in the commercial market as well as the federal, and state/local sectors.

```html
<!DOCTYPE html>
<html lang="en">
<head>
<meta charset="utf-8">
<title>Kestrel Bridge Consulting — Business Card</title>
<link rel="stylesheet" href="https://fonts.googleapis.com/css2?family=Michroma&family=Orbitron:wght@700&family=Roboto:wght@400&display=swap">
<style>
  :root {
    --canvas-bg: #e4e5e8;
    --navy-deep: #08122a;
    --navy-mid: #0f1f45;
    --card-black: #07080a;
    --silver: #c9ccd2;
    --white: #f4f6f8;
    --accent-blue: #1f8fe0;
    --accent-teal: #1fb3c9;
    --pattern-line: rgba(90, 130, 170, 0.10);
  }
  * { margin: 0; padding: 0; box-sizing: border-box; }
  html, body { width: 1200px; height: 800px; overflow: hidden; }
  body {
    background: var(--canvas-bg);
    display: flex;
    align-items: center;
    justify-content: center;
    gap: 48px;
  }
  .card {
    position: relative;
    width: 540px;
    height: 309px;
    border-radius: 4px;
    overflow: hidden;
    box-shadow: 0 10px 30px rgba(0, 0, 0, 0.18);
  }
  .card-front { background: linear-gradient(135deg, var(--navy-mid), var(--navy-deep) 70%); }
  .card-back { background: var(--card-black); }
  .network-texture {
    position: absolute;
    inset: 0;
    background:
      radial-gradient(ellipse at 15% 90%, var(--pattern-line), transparent 55%),
      radial-gradient(ellipse at 90% 20%, var(--pattern-line), transparent 50%);
  }
  .brand {
    position: absolute;
    display: flex;
    align-items: center;
    gap: 14px;
  }
  .brand-mark {
    width: 54px;
    height: 54px;
    border-radius: 50%;
    flex: none;
  }
  .brand-name {
    font-family: "Michroma", sans-serif;
    font-size: 17px;
    line-height: 1.1;
    letter-spacing: 1px;
    text-transform: uppercase;
    padding-left: 12px;
  }
  .card-front .brand { left: 138px; top: 106px; }
  .card-front .brand-mark { background: var(--silver); }
  .card-front .brand-name { color: var(--silver); border-left: 1px solid var(--silver); }
  .card-back .brand { left: 142px; top: 42px; }
  .card-back .brand-mark { background: var(--accent-teal); }
  .card-back .brand-name { color: var(--white); border-left: 1px solid var(--white); }
  .holder-row {
    position: absolute;
    left: 36px;
    right: 36px;
    top: 148px;
    display: flex;
    align-items: center;
    gap: 14px;
  }
  .holder-row .rule { flex: 1; height: 1px; background: var(--accent-blue); }
  .holder-name {
    font-family: "Orbitron", sans-serif;
    font-weight: 700;
    font-size: 20px;
    color: var(--accent-blue);
    text-transform: uppercase;
    letter-spacing: 1px;
  }
  .contact-list {
    position: absolute;
    left: 0;
    right: 0;
    top: 188px;
    list-style: none;
    display: flex;
    flex-direction: column;
    align-items: center;
    gap: 7px;
    font-family: "Roboto", sans-serif;
    font-size: 13px;
    color: var(--white);
  }
  .contact-list li { display: flex; align-items: center; gap: 7px; }
  .contact-list svg { width: 13px; height: 13px; fill: none; stroke: var(--accent-blue); stroke-width: 2; }
</style>
</head>
<body>
  <section class="card card-front" aria-label="Card front">
    <div class="network-texture" role="img" aria-label="Faint connected-node network texture"></div>
    <div class="brand">
      <span class="brand-mark"></span>
      <span class="brand-name">Kestrel<br>Bridge<br>Consulting</span>
    </div>
  </section>

  <section class="card card-back" aria-label="Card back">
    <div class="network-texture" role="img" aria-label="Faint connected-node network texture"></div>
    <div class="brand">
      <span class="brand-mark"></span>
      <span class="brand-name">Kestrel<br>Bridge<br>Consulting</span>
    </div>
    <div class="holder-row">
      <span class="rule"></span>
      <span class="holder-name">Derek Molvane</span>
      <span class="rule"></span>
    </div>
    <ul class="contact-list">
      <li>
        <svg viewBox="0 0 24 24" aria-hidden="true"><path d="M5 3h4l2 5-3 2a12 12 0 0 0 6 6l2-3 5 2v4a2 2 0 0 1-2 2A17 17 0 0 1 3 5a2 2 0 0 1 2-2z"/></svg>
        +1 (555) 218-4907
      </li>
      <li>
        <svg viewBox="0 0 24 24" aria-hidden="true"><circle cx="12" cy="12" r="9"/><path d="M3 12h18M12 3c3 3 3 15 0 18M12 3c-3 3-3 15 0 18"/></svg>
        KestrelBridgeConsulting.example
      </li>
      <li>
        <svg viewBox="0 0 24 24" aria-hidden="true"><rect x="3" y="5" width="18" height="14" rx="2"/><path d="M3 7l9 6 9-6"/></svg>
        Derek.Molvane@KestrelBridgeConsulting.example
      </li>
    </ul>
  </section>
</body>
</html>
```